Van wraps

I need 3 wrap designs to go along with the wrap you already designed. I also have a couple of small changes to that original design. Check the previous conversation for van styles and awareness things for each van.
On the back of the original van design please move the phone number down along the bottom and make bigger. Also change all phone numbers on all designs to 405-718-2459.
Please move the phone number up under the window and change to red.
Remove pink and green boxes. Instead put the pink ribbon on the door and make it say we support breast cancer awareness. On the other side put puppy and kitten on door and say adopt a pet.

```html
<!DOCTYPE html>
<html lang="en">
<head>
<meta charset="utf-8">
<title>Redfield Heating &amp; Air – Van Wrap Sides</title>
<link href="https://fonts.googleapis.com/css2?family=Montserrat:wght@700;800&display=swap" rel="stylesheet">
<style>
  :root {
    --wrap-blue: #1d5fc4;
    --wrap-blue-light: #3b8be6;
    --wrap-red: #d81e1e;
    --wrap-red-dark: #b51414;
    --body-white: #f4f4f4;
    --body-edge: #c9c9c9;
    --glass: #8d9297;
    --mark-grey: #6e6f71;
    --ink: #222222;
    --text-white: #ffffff;
    --ribbon-flag: #c8364a;
    --ribbon-gold: #f2cf3a;
    --page: #ffffff;
  }
  html, body {
    margin: 0;
    padding: 0;
    width: 1200px;
    height: 1000px;
    overflow: hidden;
    background: var(--page);
  }
  .wrap-sheet {
    display: block;
    width: 1200px;
    height: 1000px;
    font-family: "Montserrat", Arial, sans-serif;
  }
  .body-panel { fill: var(--body-white); stroke: var(--body-edge); stroke-width: 2; }
  .panel-blue { fill: url(#blueBurst); }
  .panel-red { fill: url(#redFade); }
  .panel-band { fill: none; stroke: var(--body-white); stroke-width: 10; }
  .side-glass { fill: var(--glass); }
  .brand-block { fill: var(--mark-grey); }
  .brand-name { fill: var(--text-white); font-weight: 800; }
  .brand-title { font-size: 56px; }
  .brand-sub { font-size: 20px; }
  .phone { fill: var(--text-white); font-weight: 800; font-size: 27px; letter-spacing: 1px; }
  .web { fill: var(--text-white); font-weight: 800; font-size: 30px; }
  .plate { fill: var(--ink); font-weight: 700; font-size: 20px; }
  .cause-line { fill: var(--wrap-red); font-weight: 800; font-size: 12px; }
  .cause-line-gold { fill: #4a3d00; font-weight: 800; font-size: 12px; }
  .ribbon-flag { fill: var(--ribbon-flag); }
  .ribbon-gold { fill: var(--ribbon-gold); }
</style>
</head>
<body>
<svg class="wrap-sheet" viewBox="0 0 1200 1000" xmlns="http://www.w3.org/2000/svg">
  <defs>
    <radialGradient id="blueBurst" cx="0.7" cy="0.3" r="0.9">
      <stop offset="0" stop-color="var(--wrap-blue-light)"/>
      <stop offset="1" stop-color="var(--wrap-blue)"/>
    </radialGradient>
    <linearGradient id="redFade" x1="0" y1="0" x2="0" y2="1">
      <stop offset="0" stop-color="var(--wrap-red)"/>
      <stop offset="1" stop-color="var(--wrap-red-dark)"/>
    </linearGradient>
    <clipPath id="vanOutline">
      <path d="M20,40 Q25,5 80,2 L800,2 Q850,4 880,40 L985,150 Q1000,160 1060,170 L1140,185 Q1160,190 1160,210 L1162,340 L1175,345 L1175,385 L1090,388 L1090,370 A80 80 0 0 0 930,370 L350,370 A80 80 0 0 0 190,370 L40,372 L0,366 L0,300 L10,295 L15,60 Z"/>
    </clipPath>
    <g id="vanSide">
      <path class="body-panel" d="M20,40 Q25,5 80,2 L800,2 Q850,4 880,40 L985,150 Q1000,160 1060,170 L1140,185 Q1160,190 1160,210 L1162,340 L1175,345 L1175,385 L1090,388 L1090,370 A80 80 0 0 0 930,370 L350,370 A80 80 0 0 0 190,370 L40,372 L0,366 L0,300 L10,295 L15,60 Z"/>
      <g clip-path="url(#vanOutline)">
        <path class="panel-blue" d="M0,0 L610,0 Q570,85 470,122 Q300,168 0,172 Z"/>
        <path class="panel-red" d="M0,188 Q250,165 470,152 Q565,145 640,255 Q720,355 860,420 L0,420 Z"/>
        <path class="panel-band" d="M0,180 Q250,158 470,137"/>
      </g>
      <path class="side-glass" d="M722,45 L845,45 Q860,48 868,60 L925,140 L925,152 L722,152 Z"/>
      <rect class="brand-block" x="470" y="85" width="190" height="190" rx="22" transform="rotate(-8 565 180)"/>
    </g>
  </defs>

  <g class="van van-passenger">
    <use href="#vanSide" transform="translate(10,40)"/>
    <text class="brand-name brand-title" x="108" y="108">REDFIELD</text>
    <text class="brand-name brand-sub" x="108" y="140">Heating &amp; Air Conditioning</text>
    <text class="brand-name brand-sub" x="205" y="166">Plumbing</text>
    <text class="phone" x="146" y="274">405-718-2459</text>
    <text class="web" x="385" y="364">redfieldair.com</text>
    <text class="plate" x="958" y="229">OK 40392</text>
    <rect class="ribbon-flag" x="806" y="255" width="22" height="58" rx="6" role="img" aria-label="Red, white and blue awareness ribbon for first responders"/>
    <text class="cause-line" x="817" y="336" text-anchor="middle">We Proudly Support</text>
    <text class="cause-line" x="817" y="356" text-anchor="middle">First Responders</text>
  </g>

  <g class="van van-driver">
    <use href="#vanSide" transform="translate(1190,515) scale(-1,1)"/>
    <text class="brand-name brand-title" x="760" y="600">REDFIELD</text>
    <text class="brand-name brand-sub" x="765" y="628">Heating &amp; Air Conditioning</text>
    <text class="brand-name brand-sub" x="885" y="651">Plumbing</text>
    <text class="phone" x="820" y="745">405-718-2459</text>
    <text class="web" x="552" y="839">redfieldair.com</text>
    <text class="plate" x="130" y="701">OK 40392</text>
    <rect class="ribbon-gold" x="359" y="726" width="22" height="58" rx="6" role="img" aria-label="Gold childhood cancer awareness ribbon"/>
    <text class="cause-line-gold" x="384" y="806" text-anchor="middle">We Proudly Support</text>
    <text class="cause-line-gold" x="384" y="822" text-anchor="middle">Childhood Cancer Awareness</text>
  </g>
</svg>
</body>
</html>
```